Exciting, Professional Biz Cards/Stationary for Fitness Business
Iron Ladder: Fitness and Trainings
Exciting, Professional Biz Cards/Stationary for Fitness Business - Health
Creative Brief
Use same font as used in my logo
font does not have to match logo
Professional
Mel Tarrant
Owner, Certified Personal Trainer (CPFB)
info@ironladdercoaching.example
www.ironladder-gym.example
Use the email address of "info@ironladder-gym.example" Use logo 3 on the front.
Please use Logo 11 as well as Logo 5 on back. You decide format. Also add: In-Home Personal/Special Training Outdoor Weekend Sessions Group Events www.ironladder-gym.example

```html
<!DOCTYPE html>
<html lang="en">
<head>
<meta charset="utf-8">
<title>Iron Ladder: Fitness and Trainings – Business Cards</title>
<link href="https://fonts.googleapis.com/css2?family=Open+Sans:wght@400;600;700&display=swap" rel="stylesheet">
<style>
  :root {
    --bg: #e9e7e3;
    --green: #4d7a2c;
    --green-shade: #5f8a3e;
    --ink: #3a3a3a;
    --muted: #6b6b6b;
    --white: #ffffff;
  }
  * { box-sizing: border-box; margin: 0; padding: 0; }
  html, body { width: 1200px; height: 901px; overflow: hidden; }
  body {
    background: var(--bg);
    position: relative;
    font-family: "Open Sans", Arial, sans-serif;
  }
  .card {
    position: absolute;
    width: 560px;
    height: 320px;
    box-shadow: 0 10px 28px rgba(0,0,0,.18);
    overflow: hidden;
  }

  /* Brand name: one colour, one weight, one line */
  .brand-name {
    font-family: "Open Sans", Arial, sans-serif;
    font-weight: 700;
    white-space: nowrap;
  }

  /* Back card */
  .card-back {
    left: 60px; top: 90px;
    background: var(--green);
    color: var(--white);
  }
  .card-back .brand-name {
    position: absolute; left: 30px; top: 58px;
    font-size: 13px; color: var(--white);
  }
  .services {
    position: absolute; left: 30px; top: 102px;
    list-style: none;
    font-size: 14px; line-height: 19px; font-weight: 400;
  }
  .card-back .web {
    position: absolute; left: 30px; top: 178px;
    font-size: 14px;
  }
  .team-art {
    position: absolute; right: 30px; top: 30px;
    width: 250px; height: 190px;
    background: radial-gradient(ellipse at 50% 60%, var(--green-shade), var(--green) 70%);
  }

  /* Front card */
  .card-front {
    left: 580px; top: 470px;
    background: var(--white);
    color: var(--ink);
  }
  .card-front .brand-name {
    position: absolute; left: 0; right: 0; top: 76px;
    text-align: center;
    font-size: 18px; color: var(--ink);
  }
  .rule {
    position: absolute; left: 0; right: 0; height: 2px;
    background: var(--green);
  }
  .rule-top { top: 130px; }
  .rule-bottom { top: 178px; }
  .name-band {
    position: absolute; left: 0; right: 0; top: 135px; height: 38px;
    background: var(--green); color: var(--white);
    display: flex; align-items: center; padding-left: 150px;
    font-size: 12px;
  }
  .name-band .person { font-size: 16px; font-weight: 600; }
  .name-band .divider { margin: 0 10px; font-size: 18px; font-weight: 400; }
  .contacts {
    position: absolute; left: 238px; top: 206px;
    list-style: none; font-size: 12px; line-height: 16px; color: var(--muted);
  }
  .contacts li { display: flex; align-items: center; gap: 8px; }
  .contacts svg { width: 11px; height: 11px; fill: var(--green); flex: none; }
</style>
</head>
<body>

  <section class="card card-back">
    <div class="brand-name">Iron Ladder: Fitness and Trainings</div>
    <ul class="services">
      <li>In-Home Personal/Special Training</li>
      <li>Outdoor Weekend Sessions</li>
      <li>Group Events</li>
    </ul>
    <div class="web">www.ironladder-gym.example</div>
    <div class="team-art" role="img" aria-label="Illustration of athletes celebrating with raised arms"></div>
  </section>

  <section class="card card-front">
    <div class="brand-name">Iron Ladder: Fitness and Trainings</div>
    <div class="rule rule-top"></div>
    <div class="name-band">
      <span class="person">Mel Tarrant</span>
      <span class="divider">|</span>
      <span class="title">Owner, Certified Personal Trainer (CPFB)</span>
    </div>
    <div class="rule rule-bottom"></div>
    <ul class="contacts">
      <li>
        <svg viewBox="0 0 12 12" aria-hidden="true"><path d="M2.5 1h2l1 2.6-1.3 1a6.5 6.5 0 0 0 3.2 3.2l1-1.3 2.6 1v2a1 1 0 0 1-1 1A9.5 9.5 0 0 1 1.5 2a1 1 0 0 1 1-1z"/></svg>
        555-204-7731
      </li>
      <li>
        <svg viewBox="0 0 12 12" aria-hidden="true"><path d="M1 2.5h10v7H1z M1.5 3l4.5 3.5L10.5 3" stroke="#fff" stroke-width=".8"/></svg>
        info@ironladder-gym.example
      </li>
      <li>
        <svg viewBox="0 0 12 12" aria-hidden="true"><circle cx="6" cy="6" r="5"/><path d="M1 6h10M6 1c2 2.5 2 7.5 0 10M6 1c-2 2.5-2 7.5 0 10" stroke="#fff" stroke-width=".7" fill="none"/></svg>
        www.ironladder-gym.example
      </li>
    </ul>
  </section>

</body>
</html>
```